Business card design reauest

2 sided. White on both sides

Martin Oakhurst

Ho Chi Minh, Vietnam

Cell Phone / Whatsapp/ Wechat/Zalo
1-555-382-7194
Moakhurst@kvpartsline.vn
Www.kvpartsline.vn
Www.kvpartsline.com

Industry/Entity Type

Sofa and furniture and kitchen

Contact Information for Business Card

2 sided. White on both sides Martin Oakhurst Ho Chi Minh, Vietnam Cell Phone / Whatsapp/ Wechat/Zalo 1-555-382-7194 Moakhurst@kvpartsline.vn Www.kvpartsline.vn Www.kvpartsline.com

```html
<!DOCTYPE html>
<html lang="en">
<head>
<meta charset="utf-8">
<title>KV Partsline – Business Card</title>
<link rel="stylesheet" href="https://fonts.googleapis.com/css2?family=Outfit:wght@400;800&display=swap">
<style>
  :root {
    --backdrop: #b6b49e;
    --card: #ffffff;
    --brand-green: #009846;
    --ink: #111111;
    --charcoal: #2f2d2d;
  }
  * { margin: 0; padding: 0; box-sizing: border-box; }
  html, body { width: 764px; height: 1200px; overflow: hidden; }
  body {
    background: var(--backdrop);
    font-family: "Outfit", sans-serif;
    color: var(--ink);
    position: relative;
  }
  .card {
    position: absolute;
    left: 131px;
    width: 501px;
    height: 324px;
    background: var(--card);
  }
  .card--front { top: 242px; }
  .card--back { top: 634px; }

  .accent-bar {
    position: absolute;
    left: 64px; top: 0;
    width: 25px; height: 69px;
    background: var(--brand-green);
  }
  .corner-squares .sq {
    position: absolute;
    width: 18px; height: 19px;
    border-radius: 4px;
  }
  .sq--dark { left: 471px; top: 273px; background: var(--charcoal); }
  .sq--green { left: 452px; top: 295px; background: var(--brand-green); }

  .brand-small {
    position: absolute;
    right: 22px; top: 50px;
    font-weight: 400;
    font-size: 13px;
    letter-spacing: 0.5px;
    line-height: 1;
    color: var(--brand-green);
  }

  .person-name {
    position: absolute;
    left: 0; right: 0; top: 83px;
    padding-left: 12px;
    text-align: center;
    font-weight: 800;
    font-size: 42px;
    letter-spacing: -0.8px;
    line-height: 1;
    color: var(--brand-green);
  }
  .location {
    position: absolute;
    left: 0; right: 0; top: 135px;
    text-align: center;
    font-size: 18.5px;
    line-height: 1;
  }

  .contact-list { list-style: none; }
  .contact-row {
    position: absolute;
    left: 64px;
    display: flex;
    align-items: center;
    font-size: 15px;
    line-height: 1;
  }
  .contact-row--phone { top: 176px; }
  .contact-row--email { top: 210px; }
  .contact-row--web { top: 241px; }
  .icon {
    width: 14px; height: 14px;
    flex: none;
    margin-right: 6px;
  }
  .contact-row--phone .value { margin-left: 2px; }
  .contact-row--email .icon { margin-right: 10px; }
  .contact-row--web .icon { margin-right: 11px; }

  .brand-large {
    position: absolute;
    left: 0; right: 0; top: 176px;
    text-align: center;
    font-weight: 400;
    font-size: 26px;
    letter-spacing: 1.5px;
    line-height: 1;
    color: var(--brand-green);
  }
</style>
</head>
<body>

<section class="card card--front" aria-label="Business card front">
  <div class="accent-bar"></div>
  <div class="brand-small">KV PARTSLINE</div>

  <h1 class="person-name">Martin Oakhurst</h1>
  <p class="location">Ho Chi Minh, Vietnam</p>

  <ul class="contact-list">
    <li class="contact-row contact-row--phone">
      <svg class="icon" viewBox="0 0 14 14" aria-label="Phone">
        <circle cx="7" cy="7" r="7" fill="var(--ink)"/>
        <path d="M4.3 3.4l1.2-.3.8 1.8-.8.6c.4.9 1.1 1.6 2 2l.6-.8 1.8.8-.3 1.2c-3 .1-5.4-2.3-5.3-5.3z" fill="#fff"/>
      </svg>
      <svg class="icon" viewBox="0 0 14 14" aria-label="Messaging app"><circle cx="7" cy="7" r="7" fill="var(--ink)"/></svg>
      <svg class="icon" viewBox="0 0 14 14" aria-label="Messaging app"><circle cx="7" cy="7" r="7" fill="var(--ink)"/></svg>
      <svg class="icon" viewBox="0 0 14 14" aria-label="Messaging app"><circle cx="7" cy="7" r="7" fill="var(--ink)"/></svg>
      <span class="value">1-555-382-7194</span>
    </li>
    <li class="contact-row contact-row--email">
      <svg class="icon" viewBox="0 0 14 14" aria-label="Email">
        <circle cx="7" cy="7" r="7" fill="var(--ink)"/>
        <rect x="3.5" y="4.6" width="7" height="4.8" fill="#fff"/>
        <path d="M3.5 4.6L7 7.4l3.5-2.8M3.5 9.4L6 7M10.5 9.4L8 7" stroke="var(--ink)" stroke-width="0.6" fill="none"/>
      </svg>
      <span class="value">Moakhurst@kvpartsline.vn</span>
    </li>
    <li class="contact-row contact-row--web">
      <svg class="icon" viewBox="0 0 14 14" aria-label="Website">
        <circle cx="7" cy="7" r="7" fill="var(--ink)"/>
        <g stroke="#fff" stroke-width="0.7" fill="none">
          <circle cx="7" cy="7" r="3.8"/>
          <ellipse cx="7" cy="7" rx="1.6" ry="3.8"/>
          <path d="M3.2 7h7.6M3.7 5.3h6.6M3.7 8.7h6.6"/>
        </g>
      </svg>
      <span class="value">www.kvpartsline.vn | www.kvpartsline.com</span>
    </li>
  </ul>

  <div class="corner-squares">
    <div class="sq sq--dark"></div>
    <div class="sq sq--green"></div>
  </div>
</section>

<section class="card card--back" aria-label="Business card back">
  <div class="accent-bar"></div>
  <div class="brand-large">KV PARTSLINE</div>
  <div class="corner-squares">
    <div class="sq sq--dark"></div>
    <div class="sq sq--green"></div>
  </div>
</section>

</body>
</html>
```